Business card design and logo needed

We have been operating as Ridgeline Paddock Fencing for 30 years but never had a logo and feel there is a need for one, but have no idea for a design.
We specialise in all types of rural fencing including post and wire, post and rail, electric, chainmesh and to a lesser extent, also do industrial security fencing.
Updates

Sorry, but website is ridgelinepaddock.net

No .au on the end!
My apologies

Regards, Barry

Target Market(s)

Rural/acreage property owners, particularly horse people.

Industry/Entity Type

Industrial

Contact Information for Business Card

Ridgeline Paddock Fencing Barry Lindqvist 0427 615302. Terry Lindqvist 0427 783160
Email: ridgelinepaddock@quolmail.com.au
Website: www.ridgelinepaddock.net.au

Requirements
Must have
• Would like to highlight website address - use the business card to advertise the website or to push them to check it out.

```html
<!DOCTYPE html>
<html lang="en">
<head>
<meta charset="utf-8">
<title>Ridgeline Paddock Fencing — Logo and Business Card</title>
<link rel="stylesheet" href="https://fonts.googleapis.com/css2?family=Oswald:wght@500&family=Tinos&display=swap">
<style>
  :root {
    --stage-light: #c9c9c9;
    --stage-dark: #333333;
    --ink: #1c1c1c;
    --card-white: #ececec;
    --band-black: #1a1a1a;
    --sky-blue: #2fb6ee;
  }
  * { margin: 0; padding: 0; box-sizing: border-box; }
  html, body { width: 952px; height: 1200px; overflow: hidden; }
  body { position: relative; background: var(--stage-dark); }

  .logo-stage {
    position: absolute; left: 0; top: 0;
    width: 952px; height: 532px;
    background: var(--stage-light);
    display: flex; align-items: center; justify-content: center;
  }
  .wordmark {
    display: flex; align-items: center; gap: 18px;
  }
  .wordmark-square {
    width: 34px; height: 34px; background: var(--sky-blue);
  }
  .wordmark-name {
    font-family: "Oswald", sans-serif; font-weight: 500;
    font-size: 58px; letter-spacing: 1px; text-transform: uppercase;
    color: var(--ink); line-height: 1;
  }

  .card-stage {
    position: absolute; left: 0; top: 532px;
    width: 952px; height: 668px;
    display: flex; align-items: center; justify-content: center;
  }
  .business-card {
    width: 600px; height: 343px;
    background: var(--card-white);
    display: flex; flex-direction: column;
  }
  .card-body {
    flex: 1;
    display: flex; flex-direction: column; align-items: center;
    padding-top: 40px;
  }
  .card-wordmark { gap: 12px; margin-bottom: 30px; }
  .card-wordmark .wordmark-square { width: 20px; height: 20px; }
  .card-wordmark .wordmark-name { font-size: 34px; }
  .contact-name {
    font-family: "Tinos", serif; font-size: 26px; color: var(--ink);
    text-transform: uppercase; letter-spacing: 0.5px; line-height: 1.25;
  }
  .contact-email {
    font-family: "Tinos", serif; font-size: 21px; color: var(--ink);
    line-height: 1.4;
  }
  .web-band {
    height: 66px; background: var(--band-black);
    display: flex; align-items: center; justify-content: center;
  }
  .web-address {
    font-family: "Oswald", sans-serif; font-weight: 500;
    font-size: 31px; color: var(--sky-blue); letter-spacing: 1px;
  }
</style>
</head>
<body>
  <section class="logo-stage">
    <div class="wordmark">
      <span class="wordmark-square"></span>
      <span class="wordmark-name">Ridgeline Paddock Fencing</span>
    </div>
  </section>

  <section class="card-stage">
    <article class="business-card">
      <div class="card-body">
        <div class="wordmark card-wordmark">
          <span class="wordmark-square"></span>
          <span class="wordmark-name">Ridgeline Paddock Fencing</span>
        </div>
        <p class="contact-name">Barry Lindqvist 0427 615302</p>
        <p class="contact-name">Terry Lindqvist 0427 783160</p>
        <p class="contact-email">ridgelinepaddock@quolmail.com.au</p>
      </div>
      <div class="web-band">
        <p class="web-address">WWW.RIDGELINEPADDOCK.NET</p>
      </div>
    </article>
  </section>
</body>
</html>
```